Law Firm Website

We are a small California based law firm specializing in business, corporate and litigation matters. We need to have our website redesigned. We are looking for a new and fresh look for our site, keeping in mind that we are a law firm.
What we don't want:
**the traditional "gavel" and "scales of justice" look
**anything too crazy
What we do want:
**sophisticated yet modern and fresh corporate look and feel
**samples of websites we really like:
http://www.tkrmllp.example
http://www.hollowaybrant.example/
we also like:
http://www.fentonardis.example/
http://www.qx.example/
http://www.moberly.example/
http://www.pvtr.example
http://www.npdlaw.example/
The content will be whatever is currently on our website (www.colterlawgroup.example). We will be selecting the winner based on originality and keeping the above requirements in mind. Please note that the photos that you use will be the ones that we will be using, so choose wisely because the photos will make a difference.
Target Market(s)
Corporate clients
Industry/Entity Type
Law Firm
Look and feel

```html
<!DOCTYPE html>
<html lang="en">
<head>
<meta charset="utf-8">
<title>Colter Law Group, LLP</title>
<link rel="stylesheet" href="https://fonts.googleapis.com/css2?family=Open+Sans:wght@400;600;700&family=Tinos&family=Arimo:wght@400;700&display=swap">
<style>
:root{
  --header-bg:#4a4a4b;
  --page-top:#cfcfcf;
  --page-bottom:#f3f3f3;
  --blue:#0a6fc4;
  --blue-light:#1b8fe6;
  --blue-dark:#0559a6;
  --white:#ffffff;
  --text:#555555;
  --text-soft:#666666;
  --rule:#e2e2e2;
}
*{margin:0;padding:0;box-sizing:border-box}
html,body{width:988px;height:1200px;overflow:hidden}
body{position:relative;font-family:"Open Sans",sans-serif;color:var(--text);
  background:linear-gradient(var(--page-top) 470px,var(--page-bottom) 900px,var(--page-bottom))}
.abs{position:absolute}
.header-band{left:0;top:0;width:988px;height:470px;background:var(--header-bg);border-bottom:2px solid #e8e8e8}
.brand{left:79px;top:17px;width:220px;text-align:center}
.brand-square{width:64px;height:64px;margin:0 auto;background:var(--blue-light)}
.brand-name{font-family:"Tinos",serif;font-size:22px;color:var(--white);margin-top:3px;white-space:nowrap}
.brand-tag{font-family:"Open Sans",sans-serif;font-size:11px;color:#e0e0e0;margin-top:2px}
.call{right:114px;top:20px;text-align:right;color:var(--white)}
.call-label{font-size:14px;line-height:18px}
.call-number{font-size:17px;line-height:22px}
.phone-icon{left:880px;top:26px}
.search{left:735px;top:78px;width:169px;height:28px;background:#f2f2f2;border:1px solid #d8d8d8;font-size:11px;color:#333;padding:6px 10px}
.search svg{position:absolute;right:6px;top:5px}
.search::before{content:"";position:absolute;right:26px;top:5px;width:1px;height:16px;background:#ccc}
.nav{left:79px;top:137px;width:825px;height:43px;background:linear-gradient(var(--blue-light),var(--blue));display:flex}
.nav a{display:block;height:43px;line-height:43px;text-align:center;color:var(--white);font-weight:700;font-size:11.5px;text-decoration:none;border-right:1px solid rgba(0,0,0,.18)}
.nav a.active{background:var(--blue-dark)}
.panel{left:79px;top:180px;width:825px;height:924px;background:var(--white)}
.slider{left:88px;top:188px;width:807px;height:282px;overflow:hidden;
  background:linear-gradient(180deg,#a9a49a 0%,#8e8a82 45%,#5e5b55 100%)}
.slider-caption{left:19px;top:160px;font-size:31px;font-weight:600;color:var(--white);letter-spacing:-.5px;white-space:nowrap;text-shadow:0 1px 3px rgba(0,0,0,.4)}
.slider-nav{left:357px;top:237px;width:78px;height:78px;border-radius:50%;background:var(--white)}
.slider-nav svg{position:absolute;left:0;top:0}
.col{top:505px;width:222px}
.col-title{height:24px;border-left:3px solid var(--blue);padding-left:10px;font-size:14px;line-height:24px;color:#444;text-transform:uppercase}
.col-rule{height:1px;background:var(--rule);margin-top:14px}
.col-photo{margin-top:18px;width:222px;height:98px;border:1px solid #ddd;padding:5px;box-shadow:0 1px 2px rgba(0,0,0,.1)}
.col-photo div{width:100%;height:100%}
.col-text{margin-top:14px;font-family:"Arimo",sans-serif;font-size:9.8px;line-height:18px;color:var(--text-soft);letter-spacing:-.1px}
.btn{display:block;margin:8px -2px 0 auto;width:76px;height:23px;background:var(--blue);color:var(--white);font-family:"Arimo",sans-serif;font-size:10.5px;line-height:23px;text-align:center;text-decoration:none}
.welcome{left:117px;top:825px;width:460px}
h1,h2{font-weight:400;color:var(--blue);font-size:22px;line-height:28px}
.intro{margin-top:12px;font-size:11.1px;line-height:19px;color:var(--blue)}
.body-text{margin-top:9px;font-size:11.1px;line-height:19px;color:var(--text-soft)}
.body-text+.body-text{margin-top:5px}
.news{left:641px;top:825px;width:230px}
.news-item{margin-left:2px}
.news-item h3{margin-top:13px;font-family:"Arimo",sans-serif;font-weight:400;font-size:10.5px;color:var(--blue-dark)}
.news-date{margin-top:10px;font-size:10px;color:#777}
.news-text{margin-top:6px;font-size:10.2px;line-height:18px;color:var(--text-soft)}
.news-sep{height:1px;border-top:1px dotted #bbb;margin-top:10px}
.footer-links{left:79px;top:1126px;font-size:10.5px;color:#555}
.footer-links span{color:#aaa;margin:0 5px}
.copyright{left:79px;top:1154px;font-size:10.5px;color:#555}
.social{top:1142px;width:20px;height:20px;border-radius:3px}
</style>
</head>
<body>
<div class="abs header-band"></div>

<div class="abs brand">
  <div class="brand-square"></div>
  <div class="brand-name">Colter Law Group, LLP</div>
  <div class="brand-tag">Attorneys at Law</div>
</div>

<div class="abs call">
  <div class="call-label">Call today</div>
  <div class="call-number">+71 02 5550 1234</div>
</div>
<svg class="abs phone-icon" width="24" height="32" viewBox="0 0 24 32" aria-hidden="true">
  <path d="M6 2 C3 3 1 6 2 11 C4 19 9 26 15 30 C18 31 21 30 22 28 L18 22 C17 21 15 22 14 23 C11 20 9 16 8 12 C10 11 11 10 11 8 Z" fill="#fff"/>
</svg>

<div class="abs search">Search
  <svg width="16" height="16" viewBox="0 0 16 16" aria-hidden="true"><circle cx="6.5" cy="6.5" r="4.8" fill="none" stroke="#999" stroke-width="1.8"/><path d="M10 10 L14.5 14.5" stroke="#999" stroke-width="2.4"/></svg>
</div>

<nav class="abs nav">
  <a class="active" style="width:91px" href="#">HOME</a>
  <a style="width:129px" href="#">ABOUT CLG</a>
  <a style="width:157px" href="#">PRACTICE AREAS</a>
  <a style="width:99px" href="#">LINKS</a>
  <a style="width:120px" href="#">CONTACT</a>
</nav>

<div class="abs panel"></div>

<div class="abs slider" role="img" aria-label="City skyline with high-rise towers under a hazy sky">
  <div class="abs slider-caption">We hold the national quality standards</div>
  <div class="abs slider-nav">
    <svg width="78" height="78" viewBox="0 0 78 78" aria-hidden="true">
      <path d="M30 24 L24 30 L30 36" fill="none" stroke="#111" stroke-width="3"/>
      <line x1="39" y1="14" x2="39" y2="40" stroke="#ddd"/>
      <path d="M48 24 L54 30 L48 36" fill="none" stroke="#111" stroke-width="3"/>
    </svg>
  </div>
</div>

<section class="abs col" style="left:118px">
  <div class="col-title">Business</div>
  <div class="col-rule"></div>
  <div class="col-photo"><div role="img" aria-label="Business handshake outdoors" style="background:linear-gradient(90deg,#2b3440,#9fc2e0 45%,#d8d2c4)"></div></div>
  <p class="col-text">Dipisicing elit sed do eidolorem magna aliqua. Ut enim adnostru exercitation des ullam Dipisicing el it sed do eidolorem magna aliqua magna.</p>
  <a class="btn" href="#">READ MORE</a>
</section>
<section class="abs col" style="left:374px">
  <div class="col-title">Corporate</div>
  <div class="col-rule"></div>
  <div class="col-photo"><div role="img" aria-label="Busy modern office lobby" style="background:linear-gradient(90deg,#6b6357,#a9a79e 50%,#c9772f)"></div></div>
  <p class="col-text">Dipisicing elit sed do eidolorem magna aliqua. Ut enim adnostru exercitation des ullam Dipisicing el it sed do eidolorem magna aliqua magna.</p>
  <a class="btn" href="#">READ MORE</a>
</section>
<section class="abs col" style="left:629px">
  <div class="col-title">Litigation Matters</div>
  <div class="col-rule"></div>
  <div class="col-photo"><div role="img" aria-label="Hands signing a document with a pen" style="background:linear-gradient(135deg,#3c4d6a,#b9c6d8 55%,#e9edf3)"></div></div>
  <p class="col-text">Dipisicing elit sed do eidolorem magna aliqua. Ut enim adnostru exercitation des ullam Dipisicing el it sed do eidolorem magna aliqua magna.</p>
  <a class="btn" href="#">READ MORE</a>
</section>

<section class="abs welcome">
  <h1>Welcome to Our Website Mainpage</h1>
  <p class="intro">Colter Law Group, LLP provides quality legal representation to corporate as well as individual clients in the areas of business, corporate, securities, products liability.</p>
  <p class="body-text">Our attorneys are committed to providing zealous advocacy in litigation, as well as creative approaches to difficult challenges that face our business clients. Our goal is to provide the highest level of representation and personal service to each and every client, and to meet and exceed each client's expectations. We take the time to explore and explain all viable options and keep our clients informed at every step of their legal matter.</p>
  <p class="body-text">We encourage you to contact us to discuss the development of a professional relationship. If you seek a firm that is experienced and committed to representing your best interests, then look no further.</p>
</section>

<section class="abs news">
  <h2>Latest News</h2>
  <div class="news-item">
    <h3>TYPI NON HABENT CLARITATEM INSITAM;</h3>
    <div class="news-date">26/11/2013</div>
    <p class="news-text">Typi non habent claritatem insitam; est usislegen tis in iis qui facit eorum claritatem Investigatnes.</p>
    <div class="news-sep"></div>
  </div>
  <div class="news-item">
    <h3>TYPI NON HABENT CLARITATEM INSITAM;</h3>
    <div class="news-date">26/11/2013</div>
    <p class="news-text">Typi non habent claritatem insitam; est usislegen tis in iis qui facit eorum claritatem Investigatnes.</p>
  </div>
</section>

<div class="abs footer-links">Home<span>|</span>About CLG<span>|</span>Practice Areas<span>|</span>Links<span>|</span>Contact</div>
<div class="abs copyright">Copyright &copy; 2013 &nbsp; Northgate Studio. &nbsp; All rights reserved.</div>
<div class="abs social" style="left:823px;background:#3b5a9a" role="img" aria-label="Social profile link"></div>
<div class="abs social" style="left:849px;background:#37b4e6" role="img" aria-label="Social profile link"></div>
</body>
</html>
```